Candle Box & Belly Band Design

Design Candle Box for Soy Candles along with a belly band design that can be used on off the shelf coloured boxes. It is for a premium brand of candle - so i want the packaging to reflect this. I have included must haves below.

The candle boxes will be a few different sizes, but for the purpose of the design it would be something like a cube 12 x 12 x 12 cms

The belly band for standard boxes to be something like 5cm wide on a 12 x 12 x 12cms cube box that goes all the way around the top to the bottom - holding the lid on and providing all the relevant information. Example of box with belly band uploaded

Our company Name : Hazel & Pip - our logo is uploaded

Target Market(s)

Premium Candle Buyers

Colors

Designer to choose colors to be used in the design.

Requirements
Must have
• Must have our logo - our logo can be in any colour
• Must state:
• Soy Candle, Hand Poured, Made in Melbourne,
• A space for the fragrance, size and burn time.
• For this project use Lime, Coconut & Elderfllower, 300grams, 50 Hour burn Time

```html
<!DOCTYPE html>
<html lang="en">
<head>
<meta charset="utf-8">
<title>Hazel &amp; Pip – Soy Candle Belly Bands</title>
<link rel="stylesheet" href="https://fonts.googleapis.com/css2?family=Open+Sans:wght@400;600;700&display=swap">
<style>
  :root {
    --page: #ffffff;
    --box-black: #111111;
    --box-black-soft: #1c1c1c;
    --band-silver: #cfcfcf;
    --band-silver-light: #e4e4e4;
    --band-silver-dark: #bdbdbd;
    --ink: #151515;
    --ink-muted: #2a2a2a;
  }
  * { box-sizing: border-box; margin: 0; padding: 0; }
  html, body {
    width: 1200px;
    height: 1200px;
    overflow: hidden;
    background: var(--page);
    font-family: "Open Sans", Arial, sans-serif;
    color: var(--ink);
  }
  .range {
    width: 1200px;
    height: 1200px;
    display: flex;
    align-items: center;
    justify-content: center;
    gap: 36px;
  }
  .box-face {
    position: relative;
    width: 360px;
    height: 360px;
    background: linear-gradient(160deg, var(--box-black-soft), var(--box-black) 60%);
    display: flex;
    justify-content: center;
  }
  .belly-band {
    width: 150px;
    height: 100%;
    background: linear-gradient(90deg, var(--band-silver-dark), var(--band-silver-light) 45%, var(--band-silver) 100%);
    display: flex;
    flex-direction: column;
    align-items: center;
    padding: 34px 12px 22px;
  }
  .product-type {
    font-size: 17px;
    font-weight: 600;
    line-height: 1.1;
  }
  .product-method {
    font-size: 9.5px;
    font-weight: 600;
    letter-spacing: 0.02em;
    margin-top: 3px;
  }
  .brand {
    display: flex;
    align-items: center;
    gap: 6px;
    margin-top: 70px;
  }
  .brand-dot {
    width: 10px;
    height: 10px;
    border-radius: 50%;
    background: var(--ink);
  }
  .brand-name {
    font-size: 17px;
    font-weight: 400;
    color: var(--ink-muted);
    white-space: nowrap;
  }
  .specs {
    list-style: none;
    margin-top: 42px;
    align-self: flex-start;
    padding-left: 6px;
  }
  .spec {
    display: flex;
    align-items: center;
    gap: 5px;
    font-size: 10px;
    font-weight: 600;
    line-height: 1.45;
    white-space: nowrap;
  }
  .spec svg { width: 13px; height: 13px; flex: none; }
  .spec--fragrance { font-size: 14px; font-weight: 700; }
  .origin {
    margin-top: auto;
    font-size: 9.5px;
    font-weight: 600;
  }
</style>
</head>
<body>
<main class="range">

  <article class="box-face">
    <section class="belly-band">
      <h2 class="product-type">Soy Candle</h2>
      <p class="product-method">HAND POURED</p>
      <div class="brand"><span class="brand-dot"></span><span class="brand-name">Hazel &amp; Pip</span></div>
      <ul class="specs">
        <li class="spec spec--fragrance"><svg viewBox="0 0 14 14" fill="none" stroke="currentColor" stroke-width="1"><rect x="3" y="6" width="8" height="7"/><path d="M7 6V4M7 4c-1-1 0-2.5 0-3 0 .5 1 2 0 3z"/></svg>Lime</li>
        <li class="spec"><svg viewBox="0 0 14 14" fill="none" stroke="currentColor" stroke-width="1"><path d="M7 1v12M4 13h6M2 3h10M2 3l-1.5 4h3zM12 3l-1.5 4h3z"/></svg>300grams</li>
        <li class="spec"><svg viewBox="0 0 14 14" fill="none" stroke="currentColor" stroke-width="1"><circle cx="7" cy="7" r="5.5"/><path d="M7 3.5V7l2.5 1.5"/></svg>50 Hour burn Time</li>
      </ul>
      <p class="origin">Made in Melbourne</p>
    </section>
  </article>

  <article class="box-face">
    <section class="belly-band">
      <h2 class="product-type">Soy Candle</h2>
      <p class="product-method">HAND POURED</p>
      <div class="brand"><span class="brand-dot"></span><span class="brand-name">Hazel &amp; Pip</span></div>
      <ul class="specs">
        <li class="spec spec--fragrance"><svg viewBox="0 0 14 14" fill="none" stroke="currentColor" stroke-width="1"><rect x="3" y="6" width="8" height="7"/><path d="M7 6V4M7 4c-1-1 0-2.5 0-3 0 .5 1 2 0 3z"/></svg>Coconut</li>
        <li class="spec"><svg viewBox="0 0 14 14" fill="none" stroke="currentColor" stroke-width="1"><path d="M7 1v12M4 13h6M2 3h10M2 3l-1.5 4h3zM12 3l-1.5 4h3z"/></svg>300grams</li>
        <li class="spec"><svg viewBox="0 0 14 14" fill="none" stroke="currentColor" stroke-width="1"><circle cx="7" cy="7" r="5.5"/><path d="M7 3.5V7l2.5 1.5"/></svg>50 Hour burn Time</li>
      </ul>
      <p class="origin">Made in Melbourne</p>
    </section>
  </article>

  <article class="box-face">
    <section class="belly-band">
      <h2 class="product-type">Soy Candle</h2>
      <p class="product-method">HAND POURED</p>
      <div class="brand"><span class="brand-dot"></span><span class="brand-name">Hazel &amp; Pip</span></div>
      <ul class="specs">
        <li class="spec spec--fragrance"><svg viewBox="0 0 14 14" fill="none" stroke="currentColor" stroke-width="1"><rect x="3" y="6" width="8" height="7"/><path d="M7 6V4M7 4c-1-1 0-2.5 0-3 0 .5 1 2 0 3z"/></svg>Elderfllower</li>
        <li class="spec"><svg viewBox="0 0 14 14" fill="none" stroke="currentColor" stroke-width="1"><path d="M7 1v12M4 13h6M2 3h10M2 3l-1.5 4h3zM12 3l-1.5 4h3z"/></svg>300grams</li>
        <li class="spec"><svg viewBox="0 0 14 14" fill="none" stroke="currentColor" stroke-width="1"><circle cx="7" cy="7" r="5.5"/><path d="M7 3.5V7l2.5 1.5"/></svg>50 Hour burn Time</li>
      </ul>
      <p class="origin">Made in Melbourne</p>
    </section>
  </article>

</main>
</body>
</html>
```